Professional business cards for real estate development company

I need business cards for my new real estate development company. The company, "KORVA" is a real estate development, investment, and advisory firm with a focus on multifamily, office, and mixed-use projects across primary and secondary markets in the Southeast United States.

Style preference is modern

Industry/Entity Type

Real Estate Development

Contact Information for Business Card

The business cards need to include:
Name
Title
Mailing Address
Phone Number
Web Address

Logo is attached. I would like white to be the primary color with incorporation of the company colors: #232D3A and #B5A451

Font styles to use
Other font styles liked:
• Montserrat, Avenir

Requirements
Must have
• Company Logo. No need to include the company name since the name is in the logo.
Should not have
• No line type designs

```html
<!DOCTYPE html>
<html lang="en">
<head>
<meta charset="utf-8">
<title>KORVA Business Card</title>
<link rel="stylesheet" href="https://fonts.googleapis.com/css2?family=Cinzel:wght@500&family=Montserrat:wght@200;500&family=Roboto+Condensed:wght@400&display=swap">
<style>
  :root {
    --stage: #3f3f3f;
    --paper: #ffffff;
    --navy: #232d3a;
    --navy-deep: #141b25;
    --gold: #b5a451;
    --gold-bright: #c2a63f;
    --photo-light: #d4d4d4;
    --photo-dark: #3a3a3a;
    --skyline: #1c2532;
  }
  * { box-sizing: border-box; margin: 0; padding: 0; }
  html, body {
    width: 1200px;
    height: 1200px;
    overflow: hidden;
    background: var(--stage);
  }
  .stage {
    width: 1200px;
    height: 1200px;
    display: flex;
    flex-direction: column;
    align-items: center;
    justify-content: center;
    gap: 40px;
  }
  .card {
    position: relative;
    width: 900px;
    height: 514px;
    overflow: hidden;
    border-bottom: 4px solid var(--gold-bright);
    box-shadow: 0 18px 40px rgba(0,0,0,0.35);
  }

  /* Front */
  .card--front { background: var(--paper); }
  .portrait {
    position: absolute;
    left: 0;
    bottom: 0;
    width: 290px;
    height: 400px;
    background: linear-gradient(180deg, var(--photo-light) 0%, #9a9a9a 45%, var(--photo-dark) 100%);
  }
  .nameplate {
    position: absolute;
    left: 320px;
    top: 290px;
    width: 460px;
    height: 130px;
    border: 1.5px solid var(--gold);
    display: flex;
    flex-direction: column;
    justify-content: center;
    padding-left: 50px;
  }
  .nameplate__name {
    font-family: "Cinzel", serif;
    font-weight: 500;
    font-size: 32px;
    letter-spacing: 0.22em;
    color: var(--gold);
  }
  .nameplate__title {
    font-family: "Montserrat", sans-serif;
    font-weight: 200;
    font-size: 26px;
    letter-spacing: 1.45em;
    color: var(--gold);
    margin-top: 2px;
  }

  /* Back */
  .card--back {
    background: linear-gradient(180deg, var(--navy-deep) 0%, var(--navy) 55%, #263244 100%);
  }
  .skyline {
    position: absolute;
    left: 0;
    right: 0;
    bottom: 0;
    height: 240px;
    background: linear-gradient(180deg, rgba(28,37,50,0) 0%, var(--skyline) 60%, #19212c 100%);
  }
  .infobox {
    position: absolute;
    left: 200px;
    top: 120px;
    width: 540px;
    height: 220px;
    border: 1.5px solid var(--gold);
    display: flex;
    align-items: center;
    gap: 34px;
    padding: 0 30px;
  }
  .brand {
    display: flex;
    align-items: center;
    gap: 10px;
  }
  .brand__square {
    width: 18px;
    height: 18px;
    background: var(--gold-bright);
  }
  .brand__name {
    font-family: "Montserrat", sans-serif;
    font-weight: 500;
    font-size: 44px;
    letter-spacing: 0.04em;
    color: var(--gold-bright);
  }
  .contact {
    list-style: none;
    font-family: "Roboto Condensed", sans-serif;
    font-size: 18px;
    line-height: 1.3;
    color: var(--gold-bright);
  }
  .contact__item {
    display: flex;
    align-items: flex-start;
    gap: 8px;
  }
  .contact__icon {
    flex: 0 0 16px;
    width: 16px;
    height: 16px;
    margin-top: 3px;
  }
</style>
</head>
<body>
  <main class="stage">
    <section class="card card--front" aria-label="Business card front">
      <div class="portrait" role="img" aria-label="Black and white portrait photo of the partner in a dark suit jacket and white shirt"></div>
      <div class="nameplate">
        <p class="nameplate__name">EVAN HARTLEY</p>
        <p class="nameplate__title">PARTNER</p>
      </div>
    </section>

    <section class="card card--back" aria-label="Business card back">
      <div class="skyline" role="img" aria-label="Faint navy photo of a city skyline"></div>
      <div class="infobox">
        <div class="brand">
          <span class="brand__square"></span>
          <span class="brand__name">KORVA</span>
        </div>
        <ul class="contact">
          <li class="contact__item">
            <svg class="contact__icon" viewBox="0 0 16 16" aria-hidden="true"><path d="M8 1a5 5 0 0 0-5 5c0 3.5 5 9 5 9s5-5.5 5-9a5 5 0 0 0-5-5zm0 7a2 2 0 1 1 0-4 2 2 0 0 1 0 4z" fill="currentColor"/></svg>
            <span>1480 Linden Row NE Atlanta,<br>Georgia 30309, US</span>
          </li>
          <li class="contact__item">
            <svg class="contact__icon" viewBox="0 0 16 16" aria-hidden="true"><path d="M4 1.5l2.2 3-1.3 1.6c.8 1.8 2.2 3.2 4 4l1.6-1.3 3 2.2-1.2 2.4C7 13.4 2.6 9 2.6 3.7z" fill="currentColor"/></svg>
            <span>Phone: +1-404-555-0172</span>
          </li>
          <li class="contact__item">
            <svg class="contact__icon" viewBox="0 0 16 16" aria-hidden="true"><rect x="1.5" y="3.5" width="13" height="9" fill="none" stroke="currentColor" stroke-width="1.2"/><path d="M1.5 3.5L8 9l6.5-5.5" fill="none" stroke="currentColor" stroke-width="1.2"/></svg>
            <span>EvanH@KorvaDevelopment.com</span>
          </li>
        </ul>
      </div>
    </section>
  </main>
</body>
</html>
```